Web Design - RESPONSIVE Design

People Review Site
We are in the process of building a site that reviews people in different categories (Eg Students, Politicians, actors etc.).
Ideally the design would be similar to http://brightlister.sg.lanternweave.com/ or coolpeek.com

We have the engine ready but the front end needs to be worked on and the deliverables will include HTML, Royalty Free Images and CSS for the responsive design.

Users are able to post anyone's profile (name and category combination being unique) to the site along with their comments (see profile page details below). Other users will be able to comment and will be able to vote (thumbs up and thumbs down) after logging in.
We need a design that will have the following features :
1. Home Page :
The layout should be more Web2.0 type design and should have
Search (Based on category / name / handle)
Add Profile Button -> Should take to login page that will lead to profiles management page
Login (my Account)– See Login Result Page for what happens.
Featured Listing / New / Latest Listings
A small excerpt about us with space for an introduction video
This should also have a placeholder for qv/chirpnet feed.
Bottom should have links for about us type pages - standard text pages

2. Search Results page

The results should be like tackwall – keep scrolling down and get new results.
Result should have the name/handle and the categories the person is in, thumbs up and thumbs down rating (profile voted by other people) and starting 20 words of one of the characteristics of the profile(explained below). Clicking on the result will take the user to Profile Information Page for that individual.
There needs to be a link for creating a new profile.

3. Profile Information Page

Page will have the following information about the person :
Name / Handle
Category
Comments & Supporting Information (that have been entered by the person who has created the profile)
Thumbs-up and Thumbs down count with option to vote
Followup comments by other users
Place for the user to enter his / her comments and rating

When anyone wants to post a comment about a listing, they have to connect using their email or QV account and signup – Then they will be redirected to be able to add the comments.

4. Login Results Page (Profiles Management Page)

• Show all profiles / entries that the user has created. Allow to edit the information about the profiles. Also be able to change own profile – password etc.
• Show all profiles that user has voted on or commented on.
• Link to Add New Profile

5. Add Profile Page :
• Name / Handle
• Category/Categories for this profile
• Supporting information (Pictures)
• Associated website link
• Comment Text Area for detailed review.

Target Market(s)

Typical Internet users interested in reviewing others!

Industry/Entity Type

Number of Pages Required

5+ page

Font styles to use
Serif
Sans Serif

Requirements
Must have
• Web 2.0 type design, Responsive Design
Should not have
• Should not be a pagecrate template!! We are not using a pagecrate template for our design!

```html
<!DOCTYPE html>
<html lang="en">
<head>
<meta charset="utf-8">
<title>People Reviews</title>
<link href="https://fonts.googleapis.com/css2?family=Open+Sans:wght@400;600;700&family=Lato:wght@400;700&display=swap" rel="stylesheet">
<style>
:root{
  --orange:#d9471a;
  --orange-dark:#b93a12;
  --ink:#2b2b2b;
  --text:#555;
  --muted:#8a8a8a;
  --line:#e4e4e4;
  --cream:#fdf4ee;
  --footer:#1c1c1c;
  --footer-line:#2e2e2e;
  --footer-text:#5e5e5e;
  --white:#fff;
  --star-off:#b5b5b5;
}
*{box-sizing:border-box;margin:0;padding:0}
html,body{width:1200px;height:2493px;overflow:hidden}
body{position:relative;background:var(--white);font-family:"Open Sans",Arial,sans-serif;color:var(--ink)}
a{color:inherit;text-decoration:none}
.abs{position:absolute}

/* header */
.site-header{position:absolute;left:0;top:0;width:1200px;height:96px;background:var(--white)}
.brand{left:58px;top:26px;font-size:31px;font-weight:400;color:#2a2a2a;letter-spacing:-.3px}
.main-nav{left:459px;top:36px;display:flex;align-items:center;height:27px;font-size:13px;color:#555}
.main-nav a{padding:0 14px;border-left:1px solid #aaa;line-height:13px}
.main-nav a:nth-child(2){border-left:none}
.main-nav .active{background:var(--orange);color:var(--white);width:70px;height:27px;line-height:27px;text-align:center;border:none;margin-right:2px}
.btn-logout,.btn-profile{top:37px;height:25px;line-height:25px;font-size:11px;color:var(--white);text-align:center}
.btn-logout{left:919px;width:72px;background:#333}
.btn-profile{left:994px;width:70px;background:var(--orange)}
.avatar{left:1082px;top:17px;width:46px;height:46px;border-radius:50%;background:radial-gradient(circle at 50% 40%,#d99a72,#8a4a2a);border:2px solid #f0d6c6}
.user-name{left:1072px;top:67px;font-size:12px;color:#444}

/* hero */
.hero{left:0;top:96px;width:1200px;height:612px;background:linear-gradient(180deg,#9dc0dd 0%,#c9dcea 38%,#e7e4dc 55%,#d9cbb6 80%,#cbb99f 100%)}
.search-panel{left:93px;top:321px;width:1012px;height:193px;background:rgba(70,70,70,.62)}
.search-title{left:0;top:30px;width:100%;text-align:center;font-size:30px;font-weight:700;color:var(--white)}
.search-sub{left:0;top:72px;width:100%;text-align:center;font-size:13px;color:#eee}
.field{top:116px;height:40px;background:var(--white);font-size:11px;color:#999;display:flex;align-items:center;padding-left:14px;gap:10px}
.field svg{flex:none}
.btn-search{left:794px;top:116px;width:180px;height:40px;background:var(--orange);color:var(--white);font-size:14px;text-align:center;line-height:40px}
.hero-arrow{top:379px;width:46px;height:46px;border-radius:50%;background:rgba(255,255,255,.45)}
.dots{left:0;top:723px;width:1200px;display:flex;justify-content:center;gap:8px}
.dots span{width:6px;height:6px;border-radius:50%;background:#ccc}
.dots span:first-child{background:var(--orange)}

/* welcome */
.welcome-title{left:60px;top:798px;font-size:22px;font-weight:400;color:#333}
.welcome-lead{left:60px;top:846px;width:600px;font-family:"Lato",sans-serif;font-size:16px;line-height:21px;color:#333}
.welcome-body{left:60px;top:900px;width:595px;font-family:"Lato",sans-serif;font-size:11.5px;line-height:16.6px;color:#555}
.btn-more{left:502px;top:1032px;width:145px;height:38px;background:var(--orange);color:var(--white);font-size:16px;text-align:center;line-height:38px;border-bottom:2px solid var(--orange-dark)}
.video{left:703px;top:800px;width:435px;height:270px;border:4px solid #ccc;background:linear-gradient(160deg,#b75a4a 0%,#8e4438 45%,#6d6560 75%,#4e4a48 100%);box-shadow:0 1px 4px rgba(0,0,0,.3)}
.video-bar{left:0;bottom:0;width:100%;height:28px;background:#151515;display:flex;align-items:center;padding:0 10px;gap:10px;font-size:10px;color:#ccc}
.progress{flex:1;height:3px;background:#555;position:relative}
.progress i{position:absolute;left:0;top:0;width:38%;height:3px;background:var(--orange)}

/* listings */
.listings-band{left:0;top:1107px;width:1200px;height:971px;background:var(--cream)}
.section-title{left:60px;font-size:22px;font-weight:400;color:#333}
.pager{left:1089px;display:flex;gap:4px}
.pager span{width:20px;height:21px;display:flex;align-items:center;justify-content:center}
.pager .prev{background:var(--orange)}
.pager .next{background:#555}
.cards{left:61px;display:flex;gap:25px}
.card{width:196px;height:366px;background:var(--white);box-shadow:0 1px 3px rgba(0,0,0,.15);padding:7px;text-align:center}
.photo{width:182px;height:196px}
.card h3{margin-top:10px;font-size:15px;font-weight:600;color:#222;line-height:18px}
.role{font-size:11.5px;color:#444;line-height:16px;padding-bottom:7px;border-bottom:1px solid var(--line);margin:0 4px}
.blurb{margin-top:6px;font-size:10.4px;line-height:14.4px;color:#555;padding:0 4px}
.card-foot{margin:12px 4px 0;border-top:1px solid var(--line);padding-top:8px;display:flex;align-items:center;font-size:10px;color:#666}
.card-foot .cmt{display:flex;align-items:center;gap:6px;padding-right:12px;border-right:1px solid #ccc}
.stars{padding-left:12px;font-size:13px;letter-spacing:1px;color:var(--star-off)}
.stars b{color:var(--orange);font-weight:400}

/* footer */
.site-footer{left:0;top:2078px;width:1200px;height:415px;background:var(--footer)}
.notch{left:1095px;top:2078px;width:0;height:0;border-left:10px solid transparent;border-right:10px solid transparent;border-top:10px solid var(--cream)}
.foot-head{top:2136px;font-size:21px;color:var(--white);font-weight:400}
.foot-links{left:60px;top:2208px;list-style:none;font-size:12.5px;color:#aaa;line-height:22px}
.foot-links li::before{content:"›";margin-right:10px;color:#aaa}
.contact-info{left:298px;top:2203px;font-size:13px;line-height:19px;color:var(--footer-text)}
.contact-info p{margin-bottom:14px}
.qv-box{left:623px;top:2206px;width:195px;height:179px;background:var(--white);border:1px solid #bbb;padding:6px}
.qv-head{display:flex;gap:6px;align-items:flex-start}
.qv-square{width:40px;height:40px;background:#3b5a98}
.qv-name{font-size:10px;font-weight:700;color:#3b5a98}
.qv-like{margin-top:3px;width:38px;height:15px;border:1px solid #99a;background:#eef;font-size:9px;color:#3b5a98;text-align:center;line-height:13px}
.qv-count{font-size:9px;color:#333;margin:6px 0 5px;border-top:1px solid #ddd;padding-top:5px}
.qv-grid{display:grid;grid-template-columns:repeat(4,40px);gap:5px}
.qv-grid span{height:40px}
.tweets{left:907px;top:2203px;width:240px;font-size:13px;line-height:19px;color:var(--footer-text)}
.tweets time{color:#bbb;display:block;margin-bottom:22px}
.foot-bottom{left:0;top:2423px;width:1200px;height:1px;background:var(--footer-line)}
.copyright{left:58px;top:2447px;font-size:11.5px;color:var(--footer-text)}
.social{right:58px;top:2446px;display:flex;justify-content:flex-end;gap:12px;font-size:11px;line-height:16px;color:var(--white);font-weight:600;white-space:nowrap}
</style>
</head>
<body>

<header class="site-header">
  <div class="abs brand">People Reviews</div>
  <nav class="abs main-nav">
    <a class="active" href="#">Home</a>
    <a href="#">About Us</a>
    <a href="#">Service</a>
    <a href="#">Gallery</a>
    <a href="#">Blog</a>
    <a href="#">Contact</a>
  </nav>
  <a class="abs btn-logout" href="#">Logout</a>
  <a class="abs btn-profile" href="#">My Profile</a>
  <div class="abs avatar" role="img" aria-label="User profile photo"></div>
  <div class="abs user-name">Jhon Doe &nbsp;⌄</div>
</header>

<section class="abs hero" role="img" aria-label="Woman walking a bicycle along a sunny beach">
</section>
<div class="abs hero-arrow" style="left:5px"><svg width="46" height="46"><path d="M27 14 L18 23 L27 32" stroke="#fff" stroke-width="3" fill="none"/></svg></div>
<div class="abs hero-arrow" style="left:1147px"><svg width="46" height="46"><path d="M19 14 L28 23 L19 32" stroke="#fff" stroke-width="3" fill="none"/></svg></div>

<form class="abs search-panel">
  <h1 class="abs search-title">SEARCH NOW</h1>
  <p class="abs search-sub">Lorem Ipsum is simply dummy text of the printing and typesetting industry. Lorem Ipsum typesetting</p>
  <div class="abs field" style="left:37px;width:242px">
    <svg width="10" height="10"><circle cx="5" cy="5" r="4" fill="#777"/><circle cx="5" cy="5" r="1.5" fill="#fff"/></svg>category
    <svg style="margin-left:auto;margin-right:12px" width="10" height="6"><path d="M1 1 L5 5 L9 1" stroke="#555" stroke-width="1.5" fill="none"/></svg>
  </div>
  <div class="abs field" style="left:289px;width:243px">
    <svg width="10" height="10"><circle cx="5" cy="3" r="2.5" fill="#777"/><path d="M0 10 Q5 4 10 10Z" fill="#777"/></svg>Name
  </div>
  <div class="abs field" style="left:540px;width:243px">
    <svg width="10" height="10"><circle cx="5" cy="5" r="5" fill="#777"/><rect x="4.3" y="2" width="1.4" height="4" fill="#fff"/><rect x="4.3" y="7" width="1.4" height="1.4" fill="#fff"/></svg>Handle
  </div>
  <a class="abs btn-search" href="#">SEARCH NOW</a>
</form>

<div class="abs dots"><span></span><span></span><span></span><span></span></div>

<section>
  <h2 class="abs welcome-title">WELCOME TO OUR SITE</h2>
  <p class="abs welcome-lead">Maecenas odio dui, dapibus eget pretium nec, luctus eget velit. Sed accumsan, ante a vulputate placerat, ligula ipsum efficitur arcu, nec euismod</p>
  <p class="abs welcome-body">orem ipsum dolor sit amet, consectetur adipiscing elit. Vivamus vitae tempor urna. Proin varius velit eu augue aliquam aliquam. Nunc sagittis dui vel quam tincidunt, a tempus ipsum fringilla. Nam posuere erat a neque finibus luctus. Nam at augue fermentum nisl hendrerit dictum at quis nibh. Suspendisse pharetra ornare odio sed pulvinar. Pellentesque vestibulum, lectus id finibus vestibulum, augue metus sollicitudin nisl, ac maximus tellus mauris vitae orci.</p>
  <a class="abs btn-more" href="#">Moredetail</a>
  <div class="abs video">
    <div class="abs" style="left:0;top:0;width:100%;height:238px" role="img" aria-label="Introduction video still of two friends riding bicycles in a city street"></div>
    <div class="abs video-bar">
      <svg width="14" height="14"><circle cx="7" cy="7" r="6" stroke="#ddd" stroke-width="1.5" fill="none"/><path d="M5.5 4.5 L9.5 7 L5.5 9.5Z" fill="#ddd"/></svg>
      <svg width="26" height="10"><path d="M0 3 H3 L6 0 V10 L3 7 H0Z" fill="var(--orange)"/><rect x="10" y="2" width="2" height="6" fill="var(--orange)"/><rect x="14" y="2" width="2" height="6" fill="var(--orange)"/><rect x="18" y="2" width="2" height="6" fill="var(--orange)"/><rect x="22" y="2" width="2" height="6" fill="#777"/></svg>
      <div class="progress"><i></i></div>
      <span>01:30 / 04:55</span>
      <svg width="12" height="10"><rect x="1" y="1" width="10" height="8" stroke="#ddd" fill="none"/></svg>
      <svg width="12" height="12"><circle cx="6" cy="6" r="4" stroke="#ddd" stroke-width="2.5" fill="none" stroke-dasharray="2 1.2"/></svg>
    </div>
  </div>
</section>

<div class="abs listings-band"></div>

<h2 class="abs section-title" style="top:1127px">FEATURED LISTINGS</h2>
<div class="abs pager" style="top:1132px">
  <span class="prev"><svg width="8" height="10"><path d="M6 1 L2 5 L6 9" stroke="#fff" stroke-width="1.6" fill="none"/></svg></span>
  <span class="next"><svg width="8" height="10"><path d="M2 1 L6 5 L2 9" stroke="#fff" stroke-width="1.6" fill="none"/></svg></span>
</div>
<div class="abs cards" style="top:1175px">
  <article class="card"><div class="photo" role="img" aria-label="Portrait of a smiling woman with curly hair" style="background:linear-gradient(160deg,#7fa6c4,#3d5a72)"></div><h3>Luis Zoris</h3><p class="role">Politician of lorem ipsum</p><p class="blurb">Nullam at mi eu quam semper consectetur. Integer euismod nulla placerat, semper turpis vel, varius nibh.</p><div class="card-foot"><span class="cmt"><svg width="10" height="9"><path d="M1 1 H9 V6 H4 L2 8 V6 H1Z" fill="#888"/></svg>12 comment</span><span class="stars"><b>★★★</b>★★</span></div></article>
  <article class="card"><div class="photo" role="img" aria-label="Portrait of a young man with curly hair" style="background:linear-gradient(160deg,#b8945e,#6e4a28)"></div><h3>Cmal Moor</h3><p class="role">Politician of lorem ipsum</p><p class="blurb">Nullam at mi eu quam semper consectetur. Integer euismod nulla placerat, semper turpis vel, varius nibh.</p><div class="card-foot"><span class="cmt"><svg width="10" height="9"><path d="M1 1 H9 V6 H4 L2 8 V6 H1Z" fill="#888"/></svg>12 comment</span><span class="stars">★★★★★</span></div></article>
  <article class="card"><div class="photo" role="img" aria-label="Portrait of a smiling man with dark hair" style="background:linear-gradient(160deg,#a8465a,#5c2030)"></div><h3>Stunt o brainm</h3><p class="role">Politician of lorem ipsum</p><p class="blurb">Nullam at mi eu quam semper consectetur. Integer euismod nulla placerat, semper turpis vel, varius nibh.</p><div class="card-foot"><span class="cmt"><svg width="10" height="9"><path d="M1 1 H9 V6 H4 L2 8 V6 H1Z" fill="#888"/></svg>12 comment</span><span class="stars">★★★★★</span></div></article>
  <article class="card"><div class="photo" role="img" aria-label="Portrait of a woman wearing a scarf" style="background:linear-gradient(160deg,#e2b04a,#9a5a22)"></div><h3>David las</h3><p class="role">Politician of lorem ipsum</p><p class="blurb">Nullam at mi eu quam semper consectetur. Integer euismod nulla placerat, semper turpis vel, varius nibh.</p><div class="card-foot"><span class="cmt"><svg width="10" height="9"><path d="M1 1 H9 V6 H4 L2 8 V6 H1Z" fill="#888"/></svg>12 comment</span><span class="stars">★★★★★</span></div></article>
  <article class="card"><div class="photo" role="img" aria-label="Portrait of a smiling young man" style="background:linear-gradient(160deg,#6a6a6a,#262626)"></div><h3>Keron tylor</h3><p class="role">Politician of lorem ipsum</p><p class="blurb">Nullam at mi eu quam semper consectetur. Integer euismod nulla placerat, semper turpis vel, varius nibh.</p><div class="card-foot"><span class="cmt"><svg width="10" height="9"><path d="M1 1 H9 V6 H4 L2 8 V6 H1Z" fill="#888"/></svg>12 comment</span><span class="stars">★★★★★</span></div></article>
</div>

<h2 class="abs section-title" style="top:1589px">LATEST LISTINGS</h2>
<div class="abs pager" style="top:1594px">
  <span class="prev"><svg width="8" height="10"><path d="M6 1 L2 5 L6 9" stroke="#fff" stroke-width="1.6" fill="none"/></svg></span>
  <span class="next"><svg width="8" height="10"><path d="M2 1 L6 5 L2 9" stroke="#fff" stroke-width="1.6" fill="none"/></svg></span>
</div>
<div class="abs cards" style="top:1637px">
  <article class="card"><div class="photo" role="img" aria-label="Portrait of a man in a suit" style="background:linear-gradient(160deg,#c0603a,#4a2218)"></div><h3>Luis Zoris</h3><p class="role">Politician of lorem ipsum</p><p class="blurb">Nullam at mi eu quam semper consectetur. Integer euismod nulla placerat, semper turpis vel, varius nibh.</p><div class="card-foot"><span class="cmt"><svg width="10" height="9"><path d="M1 1 H9 V6 H4 L2 8 V6 H1Z" fill="#888"/></svg>12 comment</span><span class="stars"><b>★★★</b>★★</span></div></article>
  <article class="card"><div class="photo" role="img" aria-label="Portrait of a smiling woman with dark hair" style="background:linear-gradient(160deg,#e0b648,#8a6420)"></div><h3>Cmal Moor</h3><p class="role">Politician of lorem ipsum</p><p class="blurb">Nullam at mi eu quam semper consectetur. Integer euismod nulla placerat, semper turpis vel, varius nibh.</p><div class="card-foot"><span class="cmt"><svg width="10" height="9"><path d="M1 1 H9 V6 H4 L2 8 V6 H1Z" fill="#888"/></svg>12 comment</span><span class="stars">★★★★★</span></div></article>
  <article class="card"><div class="photo" role="img" aria-label="Portrait of a man with long hair and glasses" style="background:linear-gradient(160deg,#c8c8c8,#6c6c6c)"></div><h3>Stunt o brainm</h3><p class="role">Politician of lorem ipsum</p><p class="blurb">Nullam at mi eu quam semper consectetur. Integer euismod nulla placerat, semper turpis vel, varius nibh.</p><div class="card-foot"><span class="cmt"><svg width="10" height="9"><path d="M1 1 H9 V6 H4 L2 8 V6 H1Z" fill="#888"/></svg>12 comment</span><span class="stars">★★★★★</span></div></article>
  <article class="card"><div class="photo" role="img" aria-label="Portrait of a smiling young man" style="background:linear-gradient(160deg,#d8a24a,#7a4a1e)"></div><h3>David las</h3><p class="role">Politician of lorem ipsum</p><p class="blurb">Nullam at mi eu quam semper consectetur. Integer euismod nulla placerat, semper turpis vel, varius nibh.</p><div class="card-foot"><span class="cmt"><svg width="10" height="9"><path d="M1 1 H9 V6 H4 L2 8 V6 H1Z" fill="#888"/></svg>12 comment</span><span class="stars">★★★★★</span></div></article>
  <article class="card"><div class="photo" role="img" aria-label="Portrait of a smiling woman with long hair" style="background:linear-gradient(160deg,#d8a478,#6e4228)"></div><h3>Keron tylor</h3><p class="role">Politician of lorem ipsum</p><p class="blurb">Nullam at mi eu quam semper consectetur. Integer euismod nulla placerat, semper turpis vel, varius nibh.</p><div class="card-foot"><span class="cmt"><svg width="10" height="9"><path d="M1 1 H9 V6 H4 L2 8 V6 H1Z" fill="#888"/></svg>12 comment</span><span class="stars">★★★★★</span></div></article>
</div>

<footer class="abs site-footer"></footer>
<div class="abs notch"></div>
<h4 class="abs foot-head" style="left:60px">useful links</h4>
<h4 class="abs foot-head" style="left:298px">Contact</h4>
<h4 class="abs foot-head" style="left:627px">QV Feed</h4>
<h4 class="abs foot-head" style="left:907px">Chirpnet</h4>
<ul class="abs foot-links">
  <li>Home</li><li>About Us</li><li>Service</li><li>Gallery</li><li>Blog</li><li>Contact</li>
</ul>
<div class="abs contact-info">
  <p>lorem ipsum lane ,7 Maple Grove City,<br>MG, Northland</p>
  <p>(555) 014-262-318<br>(555) 019-476-120</p>
  <p>hello@reviewhub.test<br>hello@reviewhubalternate.test</p>
</div>
<div class="abs qv-box">
  <div class="qv-head"><div class="qv-square"></div><div><div class="qv-name">QV Feed</div><div class="qv-like">Like</div></div></div>
  <div class="qv-count"><b>87,092,159</b> people like <span style="color:#3b5a98">QV Feed</span>.</div>
  <div class="qv-grid" role="img" aria-label="Grid of follower profile photos">
    <span style="background:#cfd6e2"></span><span style="background:#7a5a4a"></span><span style="background:#3a4a6a"></span><span style="background:#5a6a3a"></span>
    <span style="background:#a07a62"></span><span style="background:#6a5a6a"></span><span style="background:#8a6a5a"></span><span style="background:#4a4a4a"></span>
  </div>
</div>
<div class="abs tweets">
  <p>Nordvik - Premium Mercato Template http://ck.co/Rb7mWq2T #themegrove</p><time>about 9 hours ago</time>
  <p>Tempo - Premium Mercato Template http://ck.co/Rb7mWq2T #themegrove</p><time>about 12 hours ago</time>
</div>
<div class="abs foot-bottom"></div>
<p class="abs copyright">Copyright 2014 yoursite all rights reserved</p>
<div class="abs social">
  <span>QV</span><span>Chirpnet</span><span>Linkway</span><span>Callsky</span><span>Plusring</span><span>Designhub</span>
</div>

</body>
</html>
```